Flyer Design Project

opening a preschool and need to hand out flyers to advertise at an expo on Feb.1st. It is geared toward 3-4 year old potty trained children. I have more that 10+ years teaching experience and it will be a private preschool with small class sizes and individual instruction and attention. You can look at the website, it is www.brambleoakacademy.net. I tried to make a flyer but I can't make it with high enough resolution. I attached the logo and my attempted flyer.

Industry/Entity Type

Preschool

```html
<!DOCTYPE html>
<html lang="en">
<head>
<meta charset="utf-8">
<title>Bramble Oak Academy – Early Bird Special</title>
<link rel="stylesheet" href="https://fonts.googleapis.com/css2?family=Cinzel:wght@500&family=Marcellus&family=Delius&family=Open+Sans:wght@400;600&display=swap">
<style>
  :root {
    --teal: #36a6a4;
    --teal-dark: #2b8f8d;
    --orange: #ef6a3a;
    --brown: #4a2a1c;
    --ink: #1c1c1c;
    --body: #4d4d4d;
    --panel: #ffffff;
    --ribbon: #f4f4f4;
    --photo: #9a9a9a;
    --kids-a: #f6c86b;
    --kids-b: #f28fc0;
  }
  * { box-sizing: border-box; margin: 0; padding: 0; }
  html, body { width: 880px; height: 1200px; overflow: hidden; }
  body { background: var(--teal); font-family: "Open Sans", sans-serif; color: var(--body); }

  .flyer { position: relative; width: 880px; height: 1200px; overflow: hidden; background: var(--teal); }

  .corner-ribbon {
    position: absolute; top: 62px; right: -70px; width: 320px; height: 44px;
    background: var(--ribbon); transform: rotate(45deg);
    color: var(--orange); font: 400 19px "Delius", cursive;
    display: flex; align-items: center; justify-content: center;
  }

  .brand { position: absolute; top: 120px; left: 0; width: 880px; text-align: center; }
  .brand-dot { width: 56px; height: 56px; border-radius: 50%; background: var(--brown); margin: 0 auto 18px; }
  .brand-name { font: 500 37px "Cinzel", serif; color: var(--ink); letter-spacing: 2px; }
  .brand-tagline { margin-top: 8px; font: 400 13px "Open Sans", sans-serif; color: var(--brown); letter-spacing: 2px; }

  .content-panel { position: absolute; left: 37px; top: 282px; width: 806px; height: 860px; background: var(--panel); }

  .headline { position: absolute; top: 22px; left: 0; width: 100%; text-align: center;
    font: 400 62px "Marcellus", serif; color: var(--orange); letter-spacing: 1px; }
  .offer-line { position: absolute; top: 88px; width: 100%; text-align: center; font-size: 19px; color: var(--body); }
  .urgency { position: absolute; top: 126px; width: 100%; text-align: center; font: 400 22px "Delius", cursive; color: var(--brown); }

  .kids-illustration { position: absolute; top: 180px; left: 238px; width: 330px; height: 140px;
    border-radius: 12px; background: linear-gradient(90deg, var(--kids-a), #f7e88a 35%, var(--kids-b) 65%, #8fd0ef); opacity: .55; }

  .column { position: absolute; top: 220px; }
  .column h2 { font: 400 27px "Delius", cursive; color: var(--teal); margin-bottom: 14px; }
  .about { left: 33px; width: 362px; top: 388px; }
  .about p { font-size: 14px; line-height: 1.5; margin-bottom: 18px; }
  .offers { left: 424px; width: 360px; top: 388px; }
  .offers ul { list-style: none; }
  .offers li { position: relative; padding-left: 28px; font-size: 14px; line-height: 1.4; margin-bottom: 9px; }
  .offers li svg { position: absolute; left: 0; top: 2px; }

  .closing { position: absolute; top: 674px; width: 100%; text-align: center; font: 400 22px "Delius", cursive; color: var(--brown); }

  .teacher-photo { position: absolute; left: 33px; top: 722px; width: 112px; height: 106px;
    border: 2px solid var(--orange); border-radius: 8px; background: linear-gradient(#b8b8b8, var(--photo)); }
  .teacher-name { position: absolute; left: 160px; top: 764px; font: 400 19px "Delius", cursive; color: var(--orange); }
  .website { position: absolute; left: 160px; top: 793px; font-size: 16px; color: var(--ink); }

  .contact { position: absolute; left: 424px; top: 702px; width: 370px; }
  .contact h3 { font: 400 22px "Delius", cursive; color: var(--teal); margin-bottom: 12px; }
  .contact li { list-style: none; display: flex; align-items: center; gap: 12px; font-size: 14px; color: var(--body); margin-bottom: 12px; }

  .footnote { position: absolute; top: 1160px; width: 100%; text-align: center; font-size: 14px; color: var(--ink); }
</style>
</head>
<body>
<main class="flyer">
  <div class="corner-ribbon">Enrolling for Fall 2016!</div>

  <header class="brand">
    <div class="brand-dot"></div>
    <h1 class="brand-name">BRAMBLE OAK ACADEMY</h1>
    <p class="brand-tagline">A Foundation For The Future.</p>
  </header>

  <section class="content-panel">
    <h2 class="headline">EARLY BIRD SPECIAL!</h2>
    <p class="offer-line">Enroll before March 31st, 2016 and have your application fee waived!*</p>
    <p class="urgency">There are limited spaces! Don’t miss out!</p>

    <div class="kids-illustration" role="img" aria-label="Illustration of four happy cartoon children holding hands"></div>

    <div class="column about">
      <h2>What We’re About:</h2>
      <p>Bramble Oak Academy is a private preschool geared towards potty-trained children ages 3 to 4 years old.</p>
      <p>With a specialized curriculum, you can be assured that your child will be prepared when entering the world of education!</p>
      <p>Mrs. Whitfield is a LICENSED teacher with 10+ years of Elementary School experience. She knows what your child needs to be prepared for the rigor of K-12 education, and how to build that foundation for the future.</p>
    </div>

    <div class="column offers">
      <h2>We Offer:</h2>
      <ul>
        <li><svg width="16" height="16" viewBox="0 0 16 16"><circle cx="8" cy="8" r="8" fill="#36a6a4"/><path d="M6.5 4.5 10 8l-3.5 3.5" stroke="#fff" stroke-width="2" fill="none"/></svg>Monday through Friday classes*</li>
        <li><svg width="16" height="16" viewBox="0 0 16 16"><circle cx="8" cy="8" r="8" fill="#36a6a4"/><path d="M6.5 4.5 10 8l-3.5 3.5" stroke="#fff" stroke-width="2" fill="none"/></svg>Please call for more information on schedules</li>
        <li><svg width="16" height="16" viewBox="0 0 16 16"><circle cx="8" cy="8" r="8" fill="#36a6a4"/><path d="M6.5 4.5 10 8l-3.5 3.5" stroke="#fff" stroke-width="2" fill="none"/></svg>Competitive rates high quality education</li>
        <li><svg width="16" height="16" viewBox="0 0 16 16"><circle cx="8" cy="8" r="8" fill="#36a6a4"/><path d="M6.5 4.5 10 8l-3.5 3.5" stroke="#fff" stroke-width="2" fill="none"/></svg>Small classes, allowing for individual attention</li>
        <li><svg width="16" height="16" viewBox="0 0 16 16"><circle cx="8" cy="8" r="8" fill="#36a6a4"/><path d="M6.5 4.5 10 8l-3.5 3.5" stroke="#fff" stroke-width="2" fill="none"/></svg>Lots of creativity, discovery, and learning through play.</li>
        <li><svg width="16" height="16" viewBox="0 0 16 16"><circle cx="8" cy="8" r="8" fill="#36a6a4"/><path d="M6.5 4.5 10 8l-3.5 3.5" stroke="#fff" stroke-width="2" fill="none"/></svg>A safe, happy, fun-filled environment!</li>
      </ul>
    </div>

    <p class="closing">Students will love learning at Bramble Oak Academy!</p>

    <div class="teacher-photo" role="img" aria-label="Portrait photo of the teacher"></div>
    <p class="teacher-name">Mrs. Dana Whitfield</p>
    <p class="website">www.brambleoakacademy.net</p>

    <div class="contact">
      <h3>Contact Us &amp; Enroll Now!</h3>
      <ul>
        <li><svg width="20" height="20" viewBox="0 0 20 20"><circle cx="10" cy="10" r="10" fill="#36a6a4"/><path d="M7 5.5c.6-.4 1.2 0 1.5.6l.6 1.3c.2.5 0 .9-.4 1.2l-.5.3c.5 1.2 1.3 2 2.5 2.6l.3-.5c.3-.4.8-.6 1.2-.4l1.3.6c.6.3 1 .9.6 1.5-.6.9-1.6 1.3-2.6.9-2.6-1-4.4-2.8-5.3-5.4-.3-1 0-2 .8-2.7z" fill="#fff"/></svg>555.014.2287</li>
        <li><svg width="20" height="20" viewBox="0 0 20 20"><circle cx="10" cy="10" r="10" fill="#36a6a4"/><rect x="5" y="6.5" width="10" height="7" rx="1" fill="#fff"/><path d="M5.5 7 10 10.5 14.5 7" stroke="#36a6a4" stroke-width="1.2" fill="none"/></svg>dana@brambleoakacademy.net</li>
        <li><svg width="20" height="20" viewBox="0 0 20 20"><circle cx="10" cy="10" r="10" fill="#36a6a4"/><path d="M10 4.5a3.5 3.5 0 0 0-3.5 3.5c0 2.6 3.5 7 3.5 7s3.5-4.4 3.5-7A3.5 3.5 0 0 0 10 4.5z" fill="#fff"/><circle cx="10" cy="8" r="1.3" fill="#36a6a4"/></svg>4127 Maple Ridge Way Fairview, Colorado 80000</li>
      </ul>
    </div>
  </section>

  <p class="footnote">*You must be accepted and enrolled for application fee to be waived.</p>
</main>
</body>
</html>
```